Professional Website

We are looking for a new website for our Staffing Company. Attached is a document with all the details and pages needed along with some examples of others websites.

We want a professional Look and feel around the same color theme as the attached Vivid Vision.

We currently host our site on Pagecraft.io. If the winning designer can also add to Pagecraft, that is a plus.

```html
<!DOCTYPE html>
<html lang="en">
<head>
<meta charset="utf-8">
<title>HireBridge – Clerical &amp; Industrial Staffing</title>
<link rel="stylesheet" href="https://fonts.googleapis.com/css2?family=Poppins:ital,wght@0,400;0,500;0,600;0,700;1,400&display=swap">
<style>
  :root{
    --blue:#2440bb;
    --indigo:#2b2f9f;
    --ink:#444444;
    --white:#ffffff;
    --muted:#a9abb5;
    --footer-dark:#15151c;
    --hero-top:#4a4a4c;
    --hero-mid:#3b3a36;
    --hero-low:#2a2a2e;
  }
  *{margin:0;padding:0;box-sizing:border-box}
  html,body{width:984px;height:1200px;overflow:hidden;background:var(--white)}
  body{font-family:"Poppins",sans-serif;position:relative}
  .page{position:relative;width:984px;height:1200px;overflow:hidden}

  .hero-photo{
    position:absolute;left:0;top:0;width:984px;height:664px;
    background:
      radial-gradient(ellipse at 80% 30%, rgba(150,110,60,.45), transparent 60%),
      radial-gradient(ellipse at 50% 60%, rgba(30,30,34,.6), transparent 70%),
      linear-gradient(180deg,var(--hero-top) 0%,var(--hero-mid) 40%,var(--hero-low) 100%);
    clip-path:polygon(0 0,984px 0,984px 527px,0 664px);
  }
  .wedge{position:absolute;left:0;top:0}

  .site-header{position:absolute;left:0;top:0;width:984px;height:90px}
  .brand{position:absolute;left:67px;top:24px;color:var(--white)}
  .brand-name{font-size:36px;font-weight:600;line-height:1;letter-spacing:-1px;display:block}
  .brand-tag{font-size:9.5px;font-weight:500;letter-spacing:.6px;text-transform:uppercase;display:block;margin-top:4px}

  .top-nav{position:absolute;left:360px;top:40px;height:34px}
  .nav-item{position:absolute;top:0;height:34px}
  .nav-item svg{position:absolute;left:0;top:0}
  .nav-item span{position:absolute;top:0;height:34px;line-height:34px;font-size:10.5px;font-weight:600;color:var(--white);text-transform:uppercase;white-space:nowrap}

  .hero-title{position:absolute;left:0;top:322px;width:984px;text-align:center;color:var(--white);font-size:43px;font-weight:700;letter-spacing:-.5px}
  .cta{position:absolute;top:395px;height:49px;width:242px;border-radius:25px;color:var(--white);font-size:16.5px;font-weight:600;text-transform:uppercase;text-align:center;line-height:49px;letter-spacing:-.2px}
  .cta-job{left:243px;background:var(--indigo)}
  .cta-hire{left:499px;background:var(--blue)}

  .intro{position:absolute;left:130px;top:735px;width:724px;text-align:center;font-style:italic;font-size:17px;line-height:27.2px;color:var(--ink)}

  .footer-photo{
    position:absolute;left:0;top:0;width:984px;height:1200px;
    background:
      radial-gradient(ellipse at 70% 70%, rgba(70,60,55,.5), transparent 60%),
      linear-gradient(180deg,#2c2a2c 0%,var(--footer-dark) 60%,#101018 100%);
    clip-path:polygon(0 1025px,984px 945px,984px 1200px,0 1200px);
  }
  .areas-title{position:absolute;left:149px;top:1054px;color:var(--white);font-size:17px;font-weight:600}
  .areas{position:absolute;left:149px;top:1089px;list-style:none;color:var(--muted);font-size:14.5px;font-weight:500}
  .areas li{position:absolute;top:0;white-space:nowrap;padding-left:14px}
  .areas li::before{content:"";position:absolute;left:0;top:8px;width:6px;height:6px;border-radius:50%;background:var(--blue);border:1.5px solid var(--muted)}
  .hotline-icon{position:absolute;left:585px;top:1055px}
  .hotline-label{position:absolute;left:652px;top:1054px;color:var(--white);font-size:17px;font-weight:600}
  .hotline-number{position:absolute;left:647px;top:1080px;color:var(--white);font-size:23px;font-weight:600;letter-spacing:.3px}
  .footer-rule{position:absolute;left:149px;top:1138px;width:684px;height:1px;background:rgba(255,255,255,.12)}
  .copyright{position:absolute;left:0;top:1162px;width:984px;text-align:center;color:#dcdcdc;font-size:11px}
</style>
</head>
<body>
<div class="page">

  <div class="hero-photo" role="img" aria-label="Team of smiling business professionals in suits standing before a city skyline"></div>
  <svg class="wedge" width="984" height="1200" aria-hidden="true">
    <polygon points="295,623 984,527 984,708" fill="var(--blue)"/>
  </svg>

  <header class="site-header">
    <div class="brand">
      <span class="brand-name">HireBridge</span>
      <span class="brand-tag">Clerical &amp; Industrial</span>
    </div>
    <nav class="top-nav">
      <a class="nav-item" style="left:0;width:133px">
        <svg width="134" height="34"><polygon points="0.5,0.5 119,0.5 133,17 119,33.5 0.5,33.5" fill="none" stroke="#fff"/></svg>
        <span style="left:17px">Employee Login</span>
      </a>
      <a class="nav-item" style="left:129px;width:136px">
        <svg width="137" height="34"><polygon points="0.5,0.5 121,0.5 135,17 121,33.5 0.5,33.5 14,17" fill="none" stroke="#fff"/></svg>
        <span style="left:22px">QuickPay Login</span>
      </a>
      <a class="nav-item" style="left:262px;width:136px">
        <svg width="137" height="34"><polygon points="0.5,0.5 121,0.5 135,17 121,33.5 0.5,33.5 14,17" fill="none" stroke="#fff"/></svg>
        <span style="left:24px">Northway Login</span>
      </a>
      <a class="nav-item" style="left:394px;width:182px">
        <svg width="182" height="34"><polygon points="0.5,0.5 167,0.5 181,17 167,33.5 0.5,33.5 14,17" fill="var(--blue)" stroke="#fff"/></svg>
        <span style="left:28px">Hotline # 555-014-2270</span>
      </a>
    </nav>
  </header>

  <h1 class="hero-title">Welcome to HireBridge</h1>
  <a class="cta cta-job">I’m looking for a job</a>
  <a class="cta cta-hire">I need employees</a>

  <p class="intro">Greatest part of our daily job is that we are constantly bringing people together. Our Clients come to us in search of the perfect candidate and the job hunters approach us when they are in need of a job or looking for their next exciting role. Being able to work with and connect the two is incredibly satisfying. Not to mention that in today's current job market, employers are fighting for the top talent. This makes our employees and partners grateful for the help in finding it!</p>

  <footer>
    <div class="footer-photo" role="img" aria-label="Blurred crowd of commuters walking through a city at dusk"></div>
    <svg class="wedge" width="984" height="1200" aria-hidden="true">
      <polygon points="0,925 453,987 0,1025" fill="var(--blue)"/>
    </svg>

    <h2 class="areas-title">Areas we service</h2>
    <ul class="areas">
      <li style="left:0">Maple Ridge</li>
      <li style="left:119px">Oakdale</li>
      <li style="left:196px">Riverton</li>
    </ul>

    <svg class="hotline-icon" width="54" height="54" viewBox="0 0 54 54" aria-hidden="true">
      <circle cx="27" cy="27" r="25.5" fill="var(--blue)" stroke="#fff" stroke-width="1.5"/>
      <path d="M19.5 16.5c1-.9 2.3-.8 3 .2l2.3 3.3c.6.9.4 2-.4 2.7l-1.4 1.2c.9 2.2 3.1 4.6 5.4 5.6l1.2-1.4c.7-.8 1.9-1 2.7-.4l3.3 2.3c1 .7 1.1 2 .2 3l-1.6 1.7c-1.2 1.3-3.1 1.6-4.7.9-5.2-2.3-9.2-6.4-11.5-11.5-.7-1.6-.4-3.5.9-4.7z" fill="#fff"/>
    </svg>
    <div class="hotline-label">Hotline</div>
    <div class="hotline-number"># 555-014-2270</div>

    <div class="footer-rule"></div>
    <p class="copyright">© Copyright 2022 All Rights Reserved.</p>
  </footer>

</div>
</body>
</html>
```